Chiropractic healthcare group business card

We are a Portland Oregon based chiropractic healthcare group. Looking for a new business card design. Something cutting edge, that shows off our new logo and tag line.Use either of the attached logos.Our tag line = "Who would you be without pain?"I'm open to about anything, impress me!!
Target Market(s)
Chiropractic patients - Auto injury, back pain, sports injuries, neck , shoulder, hip, knee, ankle pain.
Industry/Entity Type
Chiropractic
Contact Information for Business Card
Dr. Bram Holtvick, D.C.
Clinic name - Fernway Chiropractic
2 clinics
location #1
20418 NW Marwick Road
Suite B
North Plains, OR 97133
Location #2
13529 SE Calloway Street
Portland OR 97236
Main phone line 971.555.0143
website : www.FernwayClinics.example
Tag line "Who would you be without pain?"
Colors
Designer to choose colors to be used in the design.
Requirements
Must have
- Use the logo colors -- Want the orange color to be a TRUE orange.
- Both clinic address
- phone number
- website
- personal email - b.holtvick@ReliefBeginsHere.example
- tag line - "Who would you be without pain?"

```html
<!DOCTYPE html>
<html lang="en">
<head>
<meta charset="UTF-8">
<title>Fernway Chiropractic – Business Card</title>
<link href="https://fonts.googleapis.com/css2?family=Lato:wght@400;700;900&display=swap" rel="stylesheet">
<style>
  :root {
    --orange: #f7941d;
    --black: #0d0d0d;
    --white: #ffffff;
    --ink: #1a1a1a;
    --grey: #2a2a2a;
    --stage: #2a2a2a;
  }
  * { margin: 0; padding: 0; box-sizing: border-box; }
  html, body { width: 1200px; height: 900px; overflow: hidden; }
  body {
    background: var(--stage);
    font-family: 'Lato', sans-serif;
    position: relative;
  }
  .card {
    position: absolute;
    left: 250px;
    width: 700px;
    height: 400px;
    background: var(--white);
    overflow: hidden;
    box-shadow: 0 10px 30px rgba(0,0,0,0.45);
  }
  .card--back { top: 40px; }
  .card--front { top: 460px; }
  .card__bg { position: absolute; inset: 0; }

  /* Back: offices */
  .offices {
    position: absolute;
    left: 60px;
    top: 95px;
    color: var(--ink);
  }
  .offices__title {
    font-weight: 900;
    font-size: 26px;
    text-decoration: underline;
    text-underline-offset: 4px;
    margin-bottom: 14px;
    color: var(--grey);
  }
  .office { margin-bottom: 22px; }
  .office__name {
    color: var(--orange);
    font-weight: 700;
    font-size: 19px;
    text-transform: uppercase;
  }
  .office__line { font-weight: 700; font-size: 16px; line-height: 1.35; }

  /* Brand name */
  .brand {
    position: absolute;
    display: flex;
    align-items: center;
    gap: 10px;
    font-weight: 900;
    text-transform: uppercase;
    line-height: 1.15;
  }
  .brand__mark { background: var(--orange); flex: none; }
  .brand--on-dark {
    right: 25px;
    top: 250px;
    color: var(--white);
    font-size: 17px;
    letter-spacing: 2px;
  }
  .brand--on-dark .brand__mark { width: 18px; height: 18px; }
  .brand--on-light {
    left: 40px;
    top: 140px;
    color: var(--black);
    font-size: 26px;
    letter-spacing: 3px;
  }
  .brand--on-light .brand__mark { width: 26px; height: 26px; }

  .tagline {
    position: absolute;
    left: 76px;
    top: 225px;
    font-weight: 700;
    font-size: 15px;
    color: var(--grey);
  }

  /* Front: contact */
  .contact {
    position: absolute;
    left: 420px;
    top: 100px;
    color: var(--ink);
  }
  .contact__name { font-weight: 900; font-size: 16px; text-transform: uppercase; }
  .contact__web { color: var(--white); font-weight: 700; font-size: 13px; margin: 3px 0 34px; }
  .contact__row {
    display: flex;
    align-items: center;
    gap: 8px;
    font-weight: 700;
    font-size: 12.5px;
    margin-bottom: 9px;
  }
  .contact__row svg { width: 14px; height: 14px; flex: none; }
  .contact__rule {
    position: absolute;
    right: 22px;
    top: 185px;
    width: 3px;
    height: 85px;
    background: var(--black);
  }
</style>
</head>
<body>

  <section class="card card--back">
    <svg class="card__bg" viewBox="0 0 700 400" aria-hidden="true">
      <polygon points="400,0 700,0 700,400 470,400" fill="#0d0d0d"/>
      <line x1="412" y1="0" x2="482" y2="400" stroke="#fff" stroke-width="3"/>
      <line x1="422" y1="0" x2="492" y2="400" stroke="#fff" stroke-width="3"/>
    </svg>
    <div class="offices">
      <h2 class="offices__title">OUR OFFICES:</h2>
      <div class="office">
        <div class="office__name">Portland Office:</div>
        <div class="office__line">13529 SE Calloway Street,</div>
        <div class="office__line">Portland OR 97236</div>
      </div>
      <div class="office">
        <div class="office__name">North Plains Office</div>
        <div class="office__line">20418 NW Marwick Road,</div>
        <div class="office__line">Suite B, North Plains, OR 97133</div>
      </div>
    </div>
    <div class="brand brand--on-dark">
      <span class="brand__mark"></span>
      <span>Fernway<br>Chiropractic</span>
    </div>
  </section>

  <section class="card card--front">
    <svg class="card__bg" viewBox="0 0 700 400" aria-hidden="true">
      <polygon points="360,0 700,0 700,400 410,400" fill="#f7941d"/>
      <line x1="364" y1="0" x2="414" y2="400" stroke="#0d0d0d" stroke-width="3"/>
      <line x1="374" y1="0" x2="424" y2="400" stroke="#0d0d0d" stroke-width="3"/>
    </svg>
    <div class="brand brand--on-light">
      <span class="brand__mark"></span>
      <span>Fernway<br>Chiropractic</span>
    </div>
    <p class="tagline">Who would you be without pain?</p>
    <div class="contact">
      <div class="contact__name">Dr. Bram Holtvick, D.C.</div>
      <div class="contact__web">www.FernwayClinics.example</div>
      <div class="contact__row">
        <svg viewBox="0 0 16 16" aria-hidden="true"><path d="M3 2h3l1 3-2 1a8 8 0 0 0 5 5l1-2 3 1v3a1 1 0 0 1-1 1A12 12 0 0 1 2 3a1 1 0 0 1 1-1z" fill="#fff"/></svg>
        (971) 555-0143
      </div>
      <div class="contact__row">
        <svg viewBox="0 0 16 16" aria-hidden="true"><rect x="2" y="6" width="12" height="7" rx="1" fill="#fff"/><rect x="4" y="2" width="8" height="4" fill="#fff"/></svg>
        (971) 555-0178
      </div>
      <div class="contact__row">
        <svg viewBox="0 0 16 16" aria-hidden="true"><rect x="1" y="3" width="14" height="10" fill="#fff"/><path d="M1 3l7 6 7-6" fill="none" stroke="#f7941d" stroke-width="1.5"/></svg>
        b.holtvick@ReliefBeginsHere.example
      </div>
    </div>
    <div class="contact__rule"></div>
  </section>

</body>
</html>
```